Stationary package for VORELO
VORELO is an outdoor and camping supplies distribution company
Professional
Yousef K Haddadin
Director
#17 Sahra Trade Gardens
Dubai
UAE
pinetrail@mailbox-ex.test
www.vorelo-supply.test

```html
<!DOCTYPE html>
<html lang="en">
<head>
<meta charset="utf-8">
<title>VORELO – Business Card</title>
<link rel="stylesheet" href="https://fonts.googleapis.com/css2?family=Archivo:ital,wght@0,400;0,600;0,800;1,400&display=swap">
<style>
  :root {
    --bg: #e7e8eb;
    --brown: #5c3313;
    --brown-light: #7a4a22;
    --white: #ffffff;
    --ink: #4a4a4a;
    --ink-soft: #6d6d6d;
  }
  * { box-sizing: border-box; margin: 0; padding: 0; }
  html, body { width: 1200px; height: 980px; overflow: hidden; }
  body {
    background: var(--bg);
    font-family: "Archivo", Arial, sans-serif;
    position: relative;
  }
  .card {
    position: absolute;
    left: 150px;
    width: 900px;
    height: 420px;
    border-radius: 26px;
    overflow: hidden;
    box-shadow: 0 10px 30px rgba(0,0,0,0.12);
  }
  .card-front { top: 50px; background: var(--white); }
  .card-back { top: 510px; background: var(--brown); }

  .front-swoosh { position: absolute; inset: 0; width: 100%; height: 100%; }

  .brand {
    position: absolute;
    left: 60px;
    top: 52px;
    display: flex;
    align-items: center;
    gap: 14px;
  }
  .brand-dot {
    width: 22px; height: 22px; border-radius: 50%;
    background: var(--brown);
  }
  .brand-name {
    font-size: 64px;
    font-weight: 800;
    letter-spacing: 1px;
    color: var(--ink);
    line-height: 1;
  }

  .contact {
    position: absolute;
    left: 60px;
    top: 190px;
    list-style: none;
  }
  .contact li {
    display: flex;
    align-items: center;
    gap: 10px;
    font-size: 15px;
    color: var(--ink);
    height: 26px;
  }
  .contact .icon {
    width: 16px; height: 16px; flex: none;
  }
  .contact .icon-blank { visibility: hidden; }

  .person {
    position: absolute;
    right: 330px;
    top: 292px;
    text-align: right;
  }
  .person-name {
    font-size: 20px;
    font-weight: 600;
    color: var(--ink);
  }
  .person-role {
    font-size: 15px;
    font-style: italic;
    color: var(--ink-soft);
    margin-top: 2px;
  }

  .back-brand {
    position: absolute;
    left: 0; right: 0; top: 150px;
    text-align: center;
    font-size: 60px;
    font-weight: 800;
    color: var(--white);
    letter-spacing: 2px;
  }
  .back-web {
    position: absolute;
    left: 0; right: 0; top: 250px;
    text-align: center;
    font-size: 16px;
    color: var(--white);
    letter-spacing: 6px;
  }
</style>
</head>
<body>

<section class="card card-front">
  <svg class="front-swoosh" viewBox="0 0 900 420" preserveAspectRatio="none" aria-hidden="true">
    <path d="M900 120 Q770 350 410 420" fill="none" stroke="var(--brown)" stroke-width="7"/>
    <path d="M900 165 Q780 370 470 420 L900 420 Z" fill="var(--brown)"/>
    <path d="M900 225 Q805 385 580 420" fill="none" stroke="var(--white)" stroke-width="12"/>
  </svg>

  <div class="brand">
    <span class="brand-name">VORELO</span>
    <span class="brand-dot"></span>
  </div>

  <ul class="contact">
    <li>
      <svg class="icon" viewBox="0 0 16 16"><circle cx="8" cy="8" r="8" fill="var(--brown)"/><path d="M8 3.5a3 3 0 0 0-3 3c0 2.2 3 6 3 6s3-3.8 3-6a3 3 0 0 0-3-3z" fill="#fff"/><circle cx="8" cy="6.5" r="1" fill="var(--brown)"/></svg>
      #17 Sahra Trade Gardens
    </li>
    <li>
      <svg class="icon icon-blank" viewBox="0 0 16 16"></svg>
      Dubai UAE
    </li>
    <li>
      <svg class="icon" viewBox="0 0 16 16"><circle cx="8" cy="8" r="8" fill="var(--brown)"/><path d="M5.5 4h1.6l.8 2-1 .8a5 5 0 0 0 2.3 2.3l.8-1 2 .8v1.6c0 .5-.4.8-.9.8A6.5 6.5 0 0 1 4.7 4.9c0-.5.3-.9.8-.9z" fill="#fff"/></svg>
      +971-50-555-0142
    </li>
    <li>
      <svg class="icon" viewBox="0 0 16 16"><circle cx="8" cy="8" r="8" fill="var(--brown)"/><path d="M5.5 4h1.6l.8 2-1 .8a5 5 0 0 0 2.3 2.3l.8-1 2 .8v1.6c0 .5-.4.8-.9.8A6.5 6.5 0 0 1 4.7 4.9c0-.5.3-.9.8-.9z" fill="#fff"/></svg>
      +971-50-555-0187
    </li>
    <li>
      <svg class="icon" viewBox="0 0 16 16"><circle cx="8" cy="8" r="8" fill="var(--brown)"/><rect x="4" y="5" width="8" height="6" rx="1" fill="#fff"/><path d="M4.3 5.4 8 8.2l3.7-2.8" fill="none" stroke="var(--brown)" stroke-width=".9"/></svg>
      pinetrail@mailbox-ex.test
    </li>
    <li>
      <svg class="icon" viewBox="0 0 16 16"><circle cx="8" cy="8" r="8" fill="var(--brown)"/><circle cx="8" cy="8" r="4" fill="none" stroke="#fff" stroke-width="1"/><path d="M4 8h8M8 4c-1.6 2.2-1.6 5.8 0 8M8 4c1.6 2.2 1.6 5.8 0 8" fill="none" stroke="#fff" stroke-width=".8"/></svg>
      www.vorelo-supply.test
    </li>
  </ul>

  <div class="person">
    <p class="person-name">Yousef K Haddadin</p>
    <p class="person-role">Director</p>
  </div>
</section>

<section class="card card-back">
  <p class="back-brand">VORELO</p>
  <p class="back-web">www.vorelo-supply.test</p>
</section>

</body>
</html>
```